Flyer-Design für den Vertrieb von Sitzbänken
Zielgruppe
Vertrieb von Valnix Sitzbänken , sich auf unsere Webseite stützen www.brelosysteme.ch,für Grundinfos.
Aufgabenstellung
Wir wollen einen Flyer haben welcher die Verschmelzung von ländlichen Umgebung und einer moderner Stadt (Smart City) darstellt. Die Sitzbank mit dem Monitor soll integriert werden und die Benefits wie :
Solarenergie,USB- und induktive Ladestation, W-Lan Internet, Nachtbeleuchtung, Monitor als Werbungsfläche müssen mit (Symbolen) aufgeführt und abgebildet. Weitere infos können auch bei www.parvoto.eu abgeholt werden.

```html
<!DOCTYPE html>
<html lang="de">
<head>
<meta charset="utf-8">
<title>Valnix Flyer – Brelo Solutions</title>
<link href="https://fonts.googleapis.com/css2?family=EB+Garamond:wght@400;500&display=swap" rel="stylesheet">
<style>
  :root {
    --page-bg: #e4e6e8;
    --flyer-bg: #000000;
    --text: #ffffff;
    --body-text: #e6e6e6;
    --accent: #3ec43a;
    --glow: #5a55ff;
    --bench: #9fb3b4;
  }
  html, body {
    margin: 0; padding: 0;
    width: 1200px; height: 900px;
    overflow: hidden;
    background: var(--page-bg);
    font-family: "EB Garamond", Georgia, serif;
  }
  .flyer {
    position: absolute;
    left: 293px; top: 20px;
    width: 696px; height: 975px;
    background: var(--flyer-bg);
    color: var(--text);
    transform: scale(0.882);
    transform-origin: top left;
    overflow: hidden;
    box-shadow: 0 8px 24px rgba(0,0,0,.25);
  }
  .brand {
    position: absolute; left: 36px; top: 40px;
    display: flex; align-items: center; gap: 14px;
  }
  .brand-dot {
    width: 62px; height: 62px; border-radius: 50%;
    background: var(--accent);
  }
  .brand-name {
    font-size: 34px; font-weight: 500; letter-spacing: 3px;
    color: var(--text); line-height: 1;
  }
  .feature { position: absolute; left: 0; width: 100%; }
  .feature-icons {
    position: absolute; left: 44px; top: 0;
    display: flex; flex-direction: column; gap: 14px;
  }
  .feature-icons svg { display: block; fill: none; stroke: var(--text); stroke-width: 2.4; stroke-linecap: round; stroke-linejoin: round; }
  .feature-title {
    position: absolute; left: 125px; top: 0; width: 478px;
    margin: 0; font-size: 22px; font-weight: 400; line-height: 28px;
    padding-bottom: 6px; border-bottom: 1.5px solid var(--accent);
  }
  .feature-text {
    position: absolute; left: 125px; top: 44px; width: 478px;
    margin: 0; font-size: 13px; line-height: 16.8px; color: var(--body-text);
  }
  .feature-text.justified { text-align: justify; }
  .w-lan { top: 170px; }
  .solar { top: 340px; }
  .monitor { top: 497px; }
  .bench-photo {
    position: absolute; left: 150px; top: 650px; width: 546px; height: 325px;
    background: linear-gradient(160deg, #000 0%, #0b0b24 40%, #2a2a8a 60%, #8fa3a5 80%, #5e6c6e 100%);
  }
  .footer {
    position: absolute; right: 16px; bottom: 2px;
    font-size: 11.5px; color: var(--text);
  }
</style>
</head>
<body>
<div class="flyer">
  <div class="brand">
    <div class="brand-dot"></div>
    <div class="brand-name">BRELO SOLUTIONS</div>
  </div>

  <section class="feature w-lan">
    <div class="feature-icons">
      <svg width="40" height="30" viewBox="0 0 40 30" aria-label="WLAN">
        <path d="M4 11 Q20 -2 36 11"/><path d="M10 17 Q20 8 30 17"/><path d="M15 22 Q20 18 25 22"/>
        <circle cx="20" cy="26" r="2" fill="#fff"/>
      </svg>
      <svg width="40" height="20" viewBox="0 0 40 20" aria-label="USB">
        <path d="M4 10 H34"/><path d="M12 10 L18 4 H24"/><path d="M16 10 L22 16 H26"/>
        <circle cx="5" cy="10" r="3" fill="#fff"/><path d="M33 7 L38 10 L33 13 Z" fill="#fff"/>
      </svg>
    </div>
    <h2 class="feature-title">W-LAN &amp; USB</h2>
    <p class="feature-text">Valnix Standard ist zu 100% solarbetrieben und benötigt keine zusätzliche Stromversorgung oder Infrastrukturellen Arbeitsaufwand. Ein speziell entwickelter Regler erzeugt 30% mehr Ausgangsleistung. An Wintertagen überwacht er die Wetterbedingungen und schaltet die Bank bei schlechtem Wetter ab. Der öffentliche Raum bekommt durch das Design eine persönliche attraktive Note, die Funktion eines</p>
  </section>

  <section class="feature solar">
    <div class="feature-icons">
      <svg width="46" height="40" viewBox="0 0 46 40" aria-label="Solarenergie">
        <circle cx="14" cy="15" r="6" fill="#fff"/>
        <path d="M14 3 V6 M14 24 V27 M2 15 H5 M23 15 H26 M6 7 L8 9 M20 21 L22 23 M22 7 L20 9 M6 23 L8 21"/>
        <path d="M30 10 V16 M38 10 V16 M27 16 H41 V22 Q41 28 34 28 Q27 28 27 22 Z M34 28 V32 Q34 37 28 37 H22"/>
      </svg>
    </div>
    <h2 class="feature-title">Solarenergie</h2>
    <p class="feature-text">Valnix Standard ist zu 100% solarbetrieben und benötigt keine zusätzliche Stromversorgung oder Infrastrukturellen Arbeitsaufwand. Ein speziell entwickelter Regler erzeugt 30% mehr Ausgangsleistung. An Wintertagen überwacht er die Wetterbedin-</p>
  </section>

  <section class="feature monitor">
    <div class="feature-icons">
      <svg width="40" height="32" viewBox="0 0 40 32" aria-label="Monitor">
        <rect x="3" y="3" width="34" height="21" rx="1.5"/><path d="M20 24 V28 M13 29 H27"/>
      </svg>
    </div>
    <h2 class="feature-title">Monitor als Werbungsfläche</h2>
    <p class="feature-text justified">Das besondere Merkmal von Valnix Urban ist ein superheller 19 Zoll Bildschirm der für das Anzeigen von Videos, Bildern oder unterschiedlicher Informationen in der Öffentlichkeit dienen kann (z. B. Wetterdaten).</p>
  </section>

  <div class="bench-photo" role="img" aria-label="Foto einer hellen Sitzbank mit blau leuchtender Solarfläche und Smartphone auf der Ladefläche bei Nacht"></div>

  <div class="footer">Brelo Solutions , CH-4600 Lindmatt.info@brelosysteme.ch, www.brelosysteme.ch</div>
</div>
</body>
</html>
```